Travesco Business Cards

We need a business card design for Travesco Mining.

This is a B2B company that buys and sells large machinery tires within the coal mining industry. The design should the strong, crisp and masculine. I have uploaded the company logo and rough mock-up of what the back of the card should look like. the front of the card should have the same look/feel as the back. I need editable templates for both the front and the back of the card.

Color scheme should be grey/green/black

Contact information to include on the card:
Name: Dale Pemberton
Title: Managing Director
Phone: 214-503-6192
Address: 1185 Wexley #3 Dallas, TX 75211
Email: Dale@Travesco-example.com

I am also opening a contest for letterhead design. If you submit a business card design, please also submit a letterhead design with the same look/feel. The winner of the business card design will also will the letter head and be paid for both.

Target Market(s)

Procurement men/women in the coal mining industry

Industry/Entity Type

Coal Mining

```html
<!DOCTYPE html>
<html lang="en">
<head>
<meta charset="utf-8">
<title>Travesco Mining Business Cards</title>
<link rel="stylesheet" href="https://fonts.googleapis.com/css2?family=Arimo:wght@400;700&display=swap">
<style>
  :root {
    --backdrop: #c9cacd;
    --card-black: #141414;
    --card-black-soft: #232323;
    --brand-green: #63b847;
    --brand-green-dark: #4f9a37;
    --ink-dark: #1d2a17;
    --white: #ffffff;
  }
  * { box-sizing: border-box; margin: 0; padding: 0; }
  html, body {
    width: 1200px; height: 900px; overflow: hidden;
    background: var(--backdrop);
    font-family: "Arimo", Arial, sans-serif;
  }
  .stage { position: relative; width: 1200px; height: 900px; }
  .card {
    position: absolute; width: 560px; height: 320px; overflow: hidden;
    background: radial-gradient(circle at 40% 30%, var(--card-black-soft), var(--card-black) 75%);
    box-shadow: 0 10px 24px rgba(0,0,0,0.25);
  }
  .card-front { left: 320px; top: 100px; }
  .card-back { left: 320px; top: 480px; }

  .wordmark { display: flex; align-items: center; gap: 14px; color: var(--white); }
  .wordmark-square { width: 22px; height: 22px; background: var(--brand-green); }
  .wordmark-name {
    font-weight: 700; font-size: 34px; letter-spacing: 2px; text-transform: uppercase;
  }

  /* front */
  .card-front .wordmark { position: absolute; left: 34px; top: 46px; }
  .front-rule { position: absolute; left: 0; right: 0; top: 122px; height: 8px; background: var(--white); }
  .front-band { position: absolute; left: 0; right: 0; top: 138px; bottom: 0; background: var(--brand-green); }
  .holder { position: absolute; left: 34px; top: 176px; }
  .holder-name { color: var(--white); font-size: 22px; text-transform: uppercase; letter-spacing: 0.5px; }
  .holder-title { color: var(--ink-dark); font-size: 11px; text-transform: uppercase; margin-top: 2px; }
  .holder-address { color: var(--ink-dark); font-size: 15px; line-height: 1.5; margin-top: 12px; }
  .contact-list { position: absolute; left: 296px; top: 160px; list-style: none; }
  .contact-list li { display: flex; align-items: baseline; gap: 6px; color: var(--ink-dark); font-size: 14.5px; line-height: 1.45; }
  .contact-label { width: 38px; text-align: right; font-size: 8px; text-transform: uppercase; color: #2f4a25; }

  /* back */
  .card-back .wordmark { position: absolute; left: 0; right: 0; top: 104px; justify-content: center; }
  .card-back .wordmark-name { font-size: 42px; }
  .back-web {
    position: absolute; left: 0; right: 0; top: 190px; text-align: center;
    color: var(--brand-green); font-size: 13px; letter-spacing: 6px; text-transform: uppercase;
  }
  .back-band { position: absolute; left: 0; right: 0; bottom: 0; height: 26px; background: var(--brand-green); }
</style>
</head>
<body>
<main class="stage">
  <section class="card card-front" aria-label="Business card front">
    <div class="wordmark">
      <span class="wordmark-square"></span>
      <span class="wordmark-name">Travesco Mining</span>
    </div>
    <div class="front-rule"></div>
    <div class="front-band"></div>
    <div class="holder">
      <p class="holder-name">Dale Pemberton</p>
      <p class="holder-title">Position</p>
      <p class="holder-address">1185 Wexley #3<br>Dallas, TX 75211</p>
    </div>
    <ul class="contact-list">
      <li><span class="contact-label">Phone</span>214.503.6192</li>
      <li><span class="contact-label">Fax</span>214.503.6193</li>
      <li><span class="contact-label">Email</span>dale@travescomining-example.com</li>
      <li><span class="contact-label">Web</span>www.travescomining-example.com</li>
    </ul>
  </section>

  <section class="card card-back" aria-label="Business card back">
    <div class="wordmark">
      <span class="wordmark-square"></span>
      <span class="wordmark-name">Travesco Mining</span>
    </div>
    <p class="back-web">www.travescomining-example.com</p>
    <div class="back-band"></div>
  </section>
</main>
</body>
</html>
```